Building Maintenance Company Capability Statement

We would like a capability statement designed please.

Let us know where we can supply the written text.

Ideally, most of the information will be on our website.
www.tidewellgroup.com.au

Target Market(s)

Strata and building managers. schools and educational facilities, retirement and aged care.

Industry/Entity Type

Building

Font styles to use
Other font styles liked:
• nanito sans light

Requirements
Must have
• Images of people working (we can supply)
Easy to skim read
Colourful and attractive
Should not have
• lots of words

```html
<!DOCTYPE html>
<html lang="en">
<head>
<meta charset="utf-8">
<title>Tidewell Group – Capabilities Statement</title>
<link href="https://fonts.googleapis.com/css2?family=Montserrat:ital,wght@0,400;0,500;0,600;0,700;1,800&family=Nunito+Sans:wght@300;400&display=swap" rel="stylesheet">
<style>
  :root {
    --navy: #0b4576;
    --red: #d2192d;
    --sky: #3c8fd0;
    --sky-soft: #6fb2e6;
    --paper: #f7f7f9;
    --ink: #333338;
    --stage: #dcdbdd;
    --white: #ffffff;
  }
  * { box-sizing: border-box; margin: 0; padding: 0; }
  html, body { width: 1200px; height: 1200px; overflow: hidden; }
  body { background: var(--stage); font-family: "Montserrat", sans-serif; color: var(--ink); }

  .sheet { position: absolute; left: 137px; top: 0; width: 926px; height: 1200px; background: var(--paper); overflow: hidden; }
  .abs { position: absolute; }

  /* header */
  .header { left: 0; top: 0; width: 926px; height: 165px; background: var(--white); }
  .brand { left: 28px; top: 44px; width: 340px; display: flex; align-items: center; gap: 12px; }
  .brand-mark { flex: none; width: 52px; height: 52px; border-radius: 50%; background: var(--navy); }
  .brand-name { font-weight: 700; font-size: 25px; color: var(--red); letter-spacing: -0.3px; white-space: nowrap; }
  .doc-title { left: 392px; top: 54px; font-weight: 800; font-style: italic; font-size: 37px; letter-spacing: -0.3px; white-space: nowrap; }
  .doc-title .lead { color: var(--red); }
  .doc-title .tail { color: var(--navy); }
  .bands { left: 0; top: 0; }

  /* photos */
  .photo { top: 165px; height: 240px; }
  .photo-wash { left: 0; width: 304px; background: linear-gradient(135deg, #e4e2dc 0%, #cfd0cb 55%, #b9d54a 80%, #a9c03a 100%); }
  .photo-paint { left: 304px; width: 318px; background: linear-gradient(160deg, #f0efea 0%, #d8d8d2 40%, #c7e04a 60%, #8c9a8c 100%); }
  .photo-deck { left: 622px; top: 149px; width: 304px; height: 256px; background: linear-gradient(150deg, #c9c5b9 0%, #c9d84a 30%, #b55a3c 60%, #9a3f28 100%); }

  .red-rule { left: 0; top: 405px; width: 926px; height: 17px; background: var(--red); }

  /* section tabs */
  .tab { left: 0; background: var(--red); color: var(--white); font-weight: 800; font-style: italic; font-size: 26px; padding-left: 42px; display: flex; align-items: center; border-radius: 0 14px 14px 0; }
  .tab-who { top: 437px; width: 267px; height: 42px; }
  .tab-why { top: 640px; width: 304px; height: 41px; }
  .tab-contact { top: 956px; width: 222px; height: 41px; }

  .intro { left: 42px; top: 500px; width: 507px; font-size: 18.4px; line-height: 22px; text-align: justify; text-align-last: left; color: #3a3a40; }

  /* values */
  .value { top: 700px; width: 118px; text-align: center; }
  .value-icon { width: 60px; height: 70px; margin: 0 auto; border-radius: 50%; background: radial-gradient(circle at 50% 45%, var(--sky-soft) 0 45%, var(--navy) 46%); }
  .value h3 { margin-top: 16px; font-weight: 500; font-size: 16px; color: #2e2e33; }
  .value p { margin-top: 6px; font-size: 12.3px; line-height: 14.6px; font-weight: 500; color: #2e2e33; }
  .v1 { left: 31px; } .v2 { left: 167px; } .v3 { left: 305px; } .v4 { left: 441px; }

  /* contact */
  .office { top: 1016px; width: 175px; }
  .office h4 { font-weight: 700; font-size: 17.5px; color: var(--navy); white-space: nowrap; }
  .office p { margin-top: 8px; font-family: "Nunito Sans", sans-serif; font-weight: 400; font-size: 16.5px; line-height: 22px; color: #444449; }
  .o1 { left: 42px; } .o2 { left: 209px; } .o3 { left: 384px; }

  /* services column */
  .services { left: 572px; top: 422px; width: 354px; height: 724px; background: var(--navy); }
  .services-head { left: 572px; top: 422px; width: 354px; height: 42px; background: var(--red); color: var(--white); font-weight: 800; font-style: italic; font-size: 26px; padding: 5px 0 0 37px; }
  .service { left: 606px; display: flex; align-items: center; gap: 22px; color: var(--white); font-weight: 700; font-size: 22.5px; line-height: 29px; }
  .service-icon { flex: none; width: 42px; height: 42px; border: 2px solid var(--white); border-radius: 4px; background: rgba(255,255,255,0.12); }

  /* footer */
  .footer-site { left: 0; top: 1146px; width: 572px; height: 54px; background: var(--navy); color: var(--white); font-weight: 700; font-size: 19.5px; display: flex; align-items: center; justify-content: center; }
  .footer-social { left: 572px; top: 1146px; width: 354px; height: 54px; background: var(--red); color: var(--white); display: flex; align-items: center; padding-left: 76px; gap: 14px; font-size: 15.5px; font-weight: 500; }
  .social-dot { width: 18px; height: 18px; border-radius: 50%; background: var(--white); }
  .social-dot:first-of-type { margin-left: 20px; }
</style>
</head>
<body>
<div class="sheet">

  <header class="abs header">
    <div class="abs brand">
      <span class="brand-mark"></span>
      <span class="brand-name">TIDEWELL GROUP</span>
    </div>
    <h1 class="abs doc-title"><span class="lead">Capabilities</span> <span class="tail">Statement:</span></h1>
  </header>

  <svg class="abs bands" width="926" height="165" viewBox="0 0 926 165">
    <path d="M400 128 C408 117 418 114 432 114 L926 114 L926 129 Z" fill="#0b4576"/>
    <rect x="0" y="129" width="926" height="20" fill="#d2192d"/>
    <path d="M0 149 L622 149 C610 160 600 164 588 164 L0 164 Z" fill="#0b4576"/>
  </svg>

  <div class="abs photo photo-wash" role="img" aria-label="Worker in hi-vis shirt pressure washing a white weatherboard wall"></div>
  <div class="abs photo photo-paint" role="img" aria-label="Worker painting a ceiling with a roller beside glass doors"></div>
  <div class="abs photo-deck" role="img" aria-label="Worker kneeling to lay new timber decking boards"></div>

  <div class="abs red-rule"></div>

  <h2 class="abs tab tab-who">Who we Are?</h2>
  <p class="abs intro">Tidewell Group is a building and painting maintenance company based in South East Qld Australia. We currently service the Sunshine Coast, Brisbane and the Gold Coast. We specialise in small to medium commercial building maintenance contracting.</p>

  <h2 class="abs tab tab-why">Why Choose Us?</h2>
  <div class="abs value v1">
    <div class="value-icon" role="img" aria-label="Award ribbon icon for 15 years"></div>
    <h3>Experienced</h3>
    <p>With an average of 15 years of building and maintenance experience, our staff are prepared to solve your challenge.</p>
  </div>
  <div class="abs value v2">
    <div class="value-icon" role="img" aria-label="Certificate document icon"></div>
    <h3>Trusted</h3>
    <p>We’re licensed, insured and police checked, so you can be secure in trusting the service we deliver.</p>
  </div>
  <div class="abs value v3">
    <div class="value-icon" role="img" aria-label="Tradesperson in hard hat icon"></div>
    <h3>Reliable</h3>
    <p>We value long-term relationships and go out of our way to please, which is why you can count on us.</p>
  </div>
  <div class="abs value v4">
    <div class="value-icon" role="img" aria-label="Verified seal with tick icon"></div>
    <h3>Willing</h3>
    <p>We’ll take on tasks that other companies have on an exclusion list.</p>
  </div>

  <h2 class="abs tab tab-contact">Contact US</h2>
  <div class="abs office o1">
    <h4>Head Office</h4>
    <p>12/4 Harbourline<br>Close, Kelvale,<br>4561<br>M: +0412555018</p>
  </div>
  <div class="abs office o2">
    <h4>Brisbane Office</h4>
    <p>3/22 Marlow Street,<br>Eastbrook QLD<br>4015<br>M: +0412555018</p>
  </div>
  <div class="abs office o3">
    <h4>Gold Coast Office</h4>
    <p>PO Box 318<br>Seacliff QLD 4221<br>M: +0412555018</p>
  </div>

  <aside class="abs services"></aside>
  <h2 class="abs services-head">Our Services</h2>
  <div class="abs service" style="top:484px"><span class="service-icon" role="img" aria-label="Flooring icon"></span>Flooring</div>
  <div class="abs service" style="top:538px"><span class="service-icon" role="img" aria-label="Plastering icon"></span>Plastering</div>
  <div class="abs service" style="top:593px"><span class="service-icon" role="img" aria-label="Paint roller icon"></span>Painting</div>
  <div class="abs service" style="top:644px"><span class="service-icon" role="img" aria-label="Plumbing pipe icon"></span>Plumbing</div>
  <div class="abs service" style="top:700px"><span class="service-icon" role="img" aria-label="Refurbishment tools icon"></span>Refurbishments</div>
  <div class="abs service" style="top:757px"><span class="service-icon" role="img" aria-label="Carpentry saw bench icon"></span>Carpentry</div>
  <div class="abs service" style="top:818px"><span class="service-icon" role="img" aria-label="Electrical plug icon"></span>Electrical</div>
  <div class="abs service" style="top:873px"><span class="service-icon" role="img" aria-label="Roof tiles icon"></span>Roofing</div>
  <div class="abs service" style="top:922px"><span class="service-icon" role="img" aria-label="Landscaped grounds icon"></span>Landscaping<br>&amp; grounds<br>maintenance</div>
  <div class="abs service" style="top:1016px"><span class="service-icon" role="img" aria-label="Building under maintenance icon"></span>Preventative<br>&amp; ongoing<br>maintenance<br>programs</div>

  <footer>
    <div class="abs footer-site">www.tidewellgroup.com.au</div>
    <div class="abs footer-social">Find us on:<span class="social-dot"></span><span class="social-dot"></span><span class="social-dot"></span></div>
  </footer>

</div>
</body>
</html>
```